Food home delivery flyer to attract new customers and drive web traffic

We need a flyer for Grubella Home Delivery for our door to door leaflet drop. The aim of our marketing is to attract new customers by driving traffic to our website and raise awareness of our service.

We want the flyer in A5, double sided, and in colour. This campaign will be primarily in print, but we need a PDF option also.

Please visit www.grubellahomedelivery.example to obtain a real feel of who we are and what we do.

The flyer should contain the Grubella Home Delivery logo, with our images to compliment our service and what we offer. All are attached to this brief, along with what wording we expect to be included in the flyer.

The main points we need to shout about are:
Sourcing fresh produce from local growers
Partnering with local businesses
Friendly team offering superior customer service
Fast, safe home delivery
Sustainable business

```html
<!DOCTYPE html>
<html lang="en">
<head>
<meta charset="utf-8">
<title>Grubella Home Delivery – A5 Double Sided Flyer</title>
<link rel="stylesheet" href="https://fonts.googleapis.com/css2?family=Arimo:ital,wght@0,400;0,700;1,400&family=Montserrat:wght@300;700&display=swap">
<style>
  :root {
    --forest: #155a38;
    --brand-green: #1d7a3c;
    --lime: #8fba3a;
    --lime-dot: #8fc640;
    --ink: #1a1a1a;
    --paper: #ffffff;
    --board: #ffffff;
    --label-grey: #d4d5d7;
    --edge: #c9c9c9;
  }
  * { box-sizing: border-box; margin: 0; padding: 0; }
  html, body { width: 1200px; height: 849px; overflow: hidden; }
  body {
    position: relative;
    background: var(--board);
    font-family: "Arimo", Arial, sans-serif;
    color: var(--ink);
  }

  .flyer {
    position: absolute;
    top: 92px;
    width: 369px;
    height: 528px;
    background: var(--paper);
    border: 1px solid var(--edge);
    box-shadow: 1px 2px 3px rgba(0,0,0,0.18);
    overflow: hidden;
  }
  .flyer--front { left: 222px; }
  .flyer--back  { left: 622px; }

  /* Front */
  .hero-photo {
    position: absolute; left: 0; top: 0; width: 100%; height: 386px;
    background: linear-gradient(160deg, #8a7a3e 0%, #7d6a3a 45%, #4f7232 100%);
  }
  .logo-panel {
    position: absolute; left: 119px; top: 0; width: 129px; height: 98px;
    background: var(--paper);
    display: flex; align-items: center; justify-content: center; text-align: center;
  }
  .brand-name {
    font-family: "Arimo", Arial, sans-serif;
    font-weight: 400;
    color: var(--brand-green);
    line-height: 1.1;
  }
  .logo-panel .brand-name { font-size: 17px; }

  .front-band {
    position: absolute; left: 0; top: 386px; width: 100%; height: 142px;
    background: var(--forest); color: var(--paper);
  }
  .front-copy {
    position: absolute; left: 31px; top: 19px; width: 172px;
    font-size: 7.3px; line-height: 9px;
  }
  .front-copy p + p { margin-top: 9px; }
  .front-url {
    position: absolute; left: 31px; top: 109px;
    font-size: 9.2px; font-weight: 700; letter-spacing: 0.1px;
  }

  .offer-badge {
    position: absolute; width: 137px; height: 137px; border-radius: 50%;
    background: var(--lime); color: var(--paper);
    display: flex; align-items: center; justify-content: center; text-align: center;
  }
  .flyer--front .offer-badge { left: 211px; top: 360px; }
  .flyer--back .offer-badge { left: 203px; top: 186px; }
  .offer-text { transform: rotate(8deg); font-weight: 700; line-height: 1; }
  .offer-headline { font-size: 22px; letter-spacing: 0.5px; }
  .offer-sub { font-size: 7.4px; margin-top: 3px; }
  .offer-note { font-size: 6.4px; font-weight: 400; margin-top: 8px; }
  .offer-code { font-size: 7.4px; margin-top: 10px; line-height: 1.25; }
  .offer-code strong { display: block; color: var(--forest); font-size: 8.4px; }
  .overleaf-arrow { display: block; margin: 4px auto 0; }

  /* Back */
  .back-logo {
    position: absolute; left: 0; top: 34px; width: 100%; text-align: center;
  }
  .back-logo .brand-name { font-size: 22px; }
  .intro {
    position: absolute; left: 22px; top: 108px; width: 322px;
    font-size: 7.3px; line-height: 9px;
  }
  .intro p + p { margin-top: 9px; }
  .benefits {
    position: absolute; left: 0; top: 180px; width: 175px; height: 88px;
    background: var(--forest); border-radius: 0 6px 6px 0;
    padding: 9px 8px 0 33px; list-style: none; color: var(--paper);
  }
  .benefits li {
    position: relative; font-size: 7.1px; font-weight: 700; line-height: 9px;
    margin-bottom: 1.6px;
  }
  .benefits li::before {
    content: ""; position: absolute; left: -11px; top: 2.5px;
    width: 4.5px; height: 4.5px; border-radius: 50%; background: var(--lime-dot);
  }
  .shop-now {
    position: absolute; left: 22px; top: 281px; width: 168px;
    font-size: 7.3px; line-height: 9px;
  }
  .shop-now em { font-style: italic; }
  .call-out {
    position: absolute; left: 22px; top: 317px;
    font-size: 7.3px; font-weight: 700;
  }
  .food-strip {
    position: absolute; left: 0; top: 347px; width: 100%; height: 128px; display: flex;
  }
  .food-photo { height: 100%; }
  .food-photo--pizza { width: 123px; background: linear-gradient(180deg, #b8623a, #8e4a30); }
  .food-photo--platter { width: 127px; background: linear-gradient(180deg, #e9d6c6, #c9917e); }
  .food-photo--salad { flex: 1; background: linear-gradient(180deg, #8a8a3e, #6c7434); }
  .back-footer {
    position: absolute; left: 22px; right: 18px; top: 495px;
    display: flex; justify-content: space-between;
    font-size: 9.2px; font-weight: 700; color: var(--forest);
  }

  /* Presentation label */
  .board-label {
    position: absolute; left: 295px; top: 673px; width: 225px; height: 176px;
    background: var(--label-grey); color: var(--paper);
    font-family: "Montserrat", Arial, sans-serif;
  }
  .board-label h1 {
    position: absolute; left: 24px; top: 27px;
    font-size: 24px; font-weight: 700; letter-spacing: 0.5px;
  }
  .board-label p {
    position: absolute; left: 24px; top: 72px;
    font-size: 13.5px; font-weight: 300; line-height: 16px;
  }
</style>
</head>
<body>

<section class="flyer flyer--front" aria-label="Flyer front">
  <div class="hero-photo" role="img" aria-label="Photo of assorted fresh vegetables and fruit"></div>
  <div class="logo-panel">
    <span class="brand-name">Grubella<br>Home Delivery</span>
  </div>
  <div class="front-band">
    <div class="front-copy">
      <p>Lovingly picked Kentish food safely delivered from our farm to your home by passionate local people who care.</p>
      <p>Avoid the supermarkets and enjoy a unique and balanced food experience with provenance.</p>
      <p>Order online for fast contactless next day delivery.</p>
    </div>
    <div class="front-url">GRUBELLAHOMEDELIVERY.EXAMPLE</div>
  </div>
  <div class="offer-badge">
    <div class="offer-text">
      <div class="offer-headline">ENJOY<br>25% OFF</div>
      <div class="offer-sub">ON ALL JULY ORDERS</div>
      <div class="offer-note">SEE OVERLEAF FOR MORE INFO</div>
      <svg class="overleaf-arrow" width="30" height="18" viewBox="0 0 30 18" aria-hidden="true">
        <path d="M2 3 C4 15, 18 17, 26 10" fill="none" stroke="#fff" stroke-width="2.4" stroke-linecap="round"/>
        <path d="M19 8 L27 9 L25 17" fill="none" stroke="#fff" stroke-width="2.4" stroke-linecap="round" stroke-linejoin="round"/>
      </svg>
    </div>
  </div>
</section>

<section class="flyer flyer--back" aria-label="Flyer back">
  <div class="back-logo">
    <span class="brand-name">Grubella<br>Home Delivery</span>
  </div>
  <div class="intro">
    <p>Grubella brings you the very best producers and growers from The Garden of England to deliver you a delicious choice for all your dining needs. From fresh produce boxes, handmade picnic boxes, fresh Kentish berry boxes to the finest local beer and wines – we’ve got it covered.</p>
    <p>Using environmentally conscious practices and minimal packaging, working hand in hand with reduced food miles brings you peace of mind with our efforts for a sustainable future.</p>
  </div>
  <ul class="benefits">
    <li>Sourcing fresh produce from local growers</li>
    <li>Partnering with local businesses</li>
    <li>Friendly team offering superior customer service</li>
    <li>Fast, safe home delivery</li>
    <li>Sustainable business</li>
  </ul>
  <div class="offer-badge">
    <div class="offer-text">
      <div class="offer-headline">ENJOY<br>25% OFF</div>
      <div class="offer-sub">ON ALL JULY ORDERS!</div>
      <div class="offer-code">ENTER CODE<strong>LOCALTOWYE</strong>AT THE CHECKOUT</div>
    </div>
  </div>
  <p class="shop-now">Shop now at <em>grubellahomedelivery.example</em><br>or call one of our friendly team at the<br>farm on <em>01632 960418</em>.</p>
  <p class="call-out">Start enjoying food with provenance now!</p>
  <div class="food-strip">
    <div class="food-photo food-photo--pizza" role="img" aria-label="Photo of a tomato and basil pizza"></div>
    <div class="food-photo food-photo--platter" role="img" aria-label="Photo of a spread of antipasti plates"></div>
    <div class="food-photo food-photo--salad" role="img" aria-label="Photo of a picnic box with salad and tarts"></div>
  </div>
  <div class="back-footer">
    <span>GRUBELLAHOMEDELIVERY.EXAMPLE</span>
    <span>PH: 01632 960418</span>
  </div>
</section>

<aside class="board-label">
  <h1>GRUBELLA</h1>
  <p>A5 DOUBLE SIDED<br>FLYER</p>
</aside>

</body>
</html>
```